<作成物>
■リッチメッセージ
リッチメニュー
合計2枚

【デザインの詳細】
デザインのイメージをファイルに入れております。
ロゴと・イメージのデザイン合わせた感じにしていただけると嬉しいです。
上下で一体感があるものを希望します。
https://22.datavault.test/0917-8a3c61f0b2d94e57c0a1d83e6b7f2c95

〈リッチメニューの表示項目〉
画像の中に入れますの、これを参考に入れてください。
この画像に似た物を作成してほしいというわけではありません。

デザイン重視でここの表示名はデザイン的に英語の方がよければ
英語でも大丈夫です。意味がわかって
ニュアンスがあっていれば文字を短くするのも
お任せします。あくまでデザイン重視です。
〈画像はこちらから〉

※こちらの作成以外に勝手に使用された場合は
著作権侵害で法的手段をとらせていただきます。
作成事例にもしようしないでください。

<サイズ>
・リッチメッセージ(1040×1040ピクセル)
・リッチメニュー(1200×810ピクセル)

<納品形式>
・ai形式(イラストレーターデータ)
・JPG
<詳細>
※添付ファイルをご確認ください。

<備考>
ブランディング効果を期待しています。
どんどん何個でも応募ください。

```html
<!DOCTYPE html>
<html lang="ja">
<head>
<meta charset="utf-8">
<title>ルミナビューティ Sora</title>
<link rel="stylesheet" href="https://fonts.googleapis.com/css2?family=Cormorant+Garamond:wght@600&family=Noto+Serif+JP:wght@400;600&family=Noto+Sans+JP:wght@400&display=swap">
<style>
:root{
  --bg-top:#eedcf2;
  --bg-mid:#d9d0ee;
  --bg-low:#e6dcef;
  --gold:#9a6e4c;
  --brown:#6b4b39;
  --tile:rgba(255,255,255,.42);
  --tile-line:rgba(205,160,190,.75);
  --deco-a:rgba(226,190,222,.55);
  --deco-b:rgba(190,214,200,.45);
  --logo:#a98cc7;
}
*{margin:0;padding:0;box-sizing:border-box}
html,body{width:720px;height:1200px;overflow:hidden}
body{
  position:relative;
  background:linear-gradient(160deg,var(--bg-top) 0%,var(--bg-mid) 45%,var(--bg-low) 100%);
  font-family:"Noto Serif JP",serif;
  color:var(--gold);
}
.deco-area{position:absolute;background:linear-gradient(135deg,var(--deco-a),var(--deco-b))}
.deco-top-left{left:0;top:0;width:230px;height:250px}
.deco-right{right:0;top:420px;width:120px;height:300px}

.logo{position:absolute;top:70px;left:0;width:720px;text-align:center}
.logo-mark{display:inline-flex;align-items:center;gap:14px;
  font-family:"Cormorant Garamond",serif;font-weight:600;font-size:78px;color:var(--logo)}
.logo-mark::before{content:"";width:22px;height:22px;border-radius:50%;background:var(--logo)}

.title{position:absolute;top:342px;left:0;width:720px;text-align:center;color:var(--gold);font-weight:600}
.title-kana{font-size:40px;letter-spacing:2px;line-height:1.2}
.title-name{font-family:"Cormorant Garamond",serif;font-size:66px;line-height:1.1}

.menu{position:absolute;left:10px;top:732px;width:700px;height:461px;
  display:grid;grid-template-columns:repeat(3,1fr);grid-template-rows:repeat(2,1fr);gap:14px 12px}
.tile{background:var(--tile);border:3px solid var(--tile-line);
  display:flex;flex-direction:column;align-items:center;justify-content:center;color:var(--brown)}
.shop-kind{font-family:"Noto Sans JP",sans-serif;font-size:18px;color:var(--gold);white-space:nowrap}
.shop-name{font-family:"Cormorant Garamond",serif;font-weight:600;font-size:62px;line-height:1.05;color:var(--brown)}
.shop-area{font-family:"Noto Sans JP",sans-serif;font-size:18px;color:var(--gold)}
.menu-icon{height:120px;display:flex;align-items:center;justify-content:center}
.menu-label{font-family:"Noto Sans JP",sans-serif;font-size:22px;margin-top:18px;color:var(--gold)}
.people{width:150px;height:118px;border-radius:20px;
  background:linear-gradient(180deg,#f7e6d2,#f2c9a8)}
</style>
</head>
<body>
  <div class="deco-area deco-top-left" role="img" aria-label="花と葉のイラスト"></div>
  <div class="deco-area deco-right" role="img" aria-label="花と葉のイラスト"></div>

  <header class="logo">
    <span class="logo-mark">Sora</span>
  </header>

  <h1 class="title">
    <div class="title-kana">ルミナビューティ</div>
    <div class="title-name">Sora</div>
  </h1>

  <nav class="menu">
    <div class="tile">
      <span class="shop-kind">セラピー＆スクール</span>
      <span class="shop-name">Sora</span>
      <span class="shop-area">海浜店</span>
    </div>
    <div class="tile">
      <div class="menu-icon">
        <svg width="130" height="110" viewBox="0 0 130 110">
          <rect x="6" y="4" width="56" height="96" rx="10" fill="var(--brown)"/>
          <rect x="14" y="18" width="40" height="64" rx="3" fill="#f4e6d6"/>
          <rect x="74" y="36" width="46" height="68" rx="8" fill="var(--brown)"/>
          <rect x="81" y="46" width="32" height="46" rx="3" fill="#f4e6d6"/>
        </svg>
      </div>
      <span class="menu-label">SNS</span>
    </div>
    <div class="tile">
      <div class="menu-icon">
        <svg width="110" height="110" viewBox="0 0 110 110" fill="none" stroke="var(--brown)" stroke-width="5">
          <rect x="8" y="18" width="94" height="84" rx="8"/>
          <line x1="8" y1="40" x2="102" y2="40"/>
          <line x1="30" y1="6" x2="30" y2="28" stroke-linecap="round"/>
          <line x1="80" y1="6" x2="80" y2="28" stroke-linecap="round"/>
          <g stroke-width="3"><line x1="8" y1="62" x2="102" y2="62"/><line x1="8" y1="82" x2="102" y2="82"/>
          <line x1="40" y1="40" x2="40" y2="102"/><line x1="70" y1="40" x2="70" y2="102"/></g>
        </svg>
      </div>
      <span class="menu-label">スクール情報</span>
    </div>
    <div class="tile">
      <span class="shop-kind">ルミナビューティー</span>
      <span class="shop-name">Sora</span>
      <span class="shop-area">山手店</span>
    </div>
    <div class="tile">
      <div class="menu-icon">
        <div class="people" role="img" aria-label="二人の人物が話しているイラスト"></div>
      </div>
      <span class="menu-label">紹介をする</span>
    </div>
    <div class="tile">
      <div class="menu-icon">
        <svg width="110" height="110" viewBox="0 0 110 110">
          <path d="M22 14c6-4 12-3 15 2l10 18c3 5 1 10-4 13l-6 4c4 12 14 24 26 30l5-6c3-4 8-5 13-2l17 11c5 3 6 9 2 14l-6 7c-5 5-12 6-20 3C48 96 18 66 10 38c-2-8 0-15 5-19z" fill="var(--brown)"/>
          <g fill="none" stroke="var(--brown)" stroke-width="5" stroke-linecap="round">
            <path d="M62 28a22 22 0 0 1 20 20"/><path d="M64 10a40 40 0 0 1 36 36"/>
          </g>
        </svg>
      </div>
      <span class="menu-label">電話予約</span>
    </div>
  </nav>
</body>
</html>
```